Holiday Let Property Management Service and Website. We manage properties for holiday letting

We want a stylish business card that reflects our brand.
*** UPDATE *** PLEASE USE THE RECTANGULAR ORANGE COLOUR SWIPE PROVIDED IN THE DROP BOX FOR THE BSINESS CARD COLOUR.***
Please view the site: www.lodgewell.com.au
Obviously, we want to use the same logo font from our site for the card design.
We want to have the name "Lodgewell" right across the front in white and an orange background colour that matches the orange on our website or a brighter fresher looking orange .
We'd like to have the details on the back similar to what I've shown below but obviously with some more aesthetic added and better positioning than I have provided.
Same colours as the front. white writing and orange background. Once we have the design we'd like the font to be raised and the finish to be a low sheen. Quality thickness and finishes.
---------------------------------------------------------------------------
(Rough idea of writing details on back of card but open to nicer repositioning)

LODGEWELL
Holiday Let Management & Consulting Specialists

Marta Van Kerr Owen Brisk
Principal Director
0492637058 0487350216

email: enquiries@lodgewell.com.au
www.lodgewell.com.au

--------------------------------------------------------------------------

Target Market(s)

Property owners who may want to convert to holiday letting and people seeking holiday accommodation.

Industry/Entity Type

Tourism

Contact Information for Business Card

(Front of card) To have "Lodgewell" to stretch across the card in white writing the same font as our website home page. (discreetly including the logo TM if possible)

------------------------------------------------------------------------------------------------
(Back of card)

LODGEWELL
Holiday Let Consultants & Management Specialists

Marta Van Kerr Owen Brisk
Principal Director
0492637058 0487350216

www.lodgewell.com.au

-----------------------------------------------------------------------------------------------

Font styles to use
Other font styles liked:
• something similar or complimentary to our logo font please

Requirements
Must have
• The same font for our logo name and close to the same colour orange as the orange footer on our website. (if you can make it pop more without going too far away from it that would be great.)
• Orange background front and back with white font.
• *** UPDATE *** PLEASE USE THE RECTANGULAR ORANGE COLOUR SWIPE PROVIDED IN THE DROP BOX FOR THE BSINESS CARD COLOUR.***
Nice to have
• Great symmetry and aesthetics
Should not have
• Any other writing except our brand name (Lodgewell) on the front of the card and a small, discreet trade mark (TM)

```html
<!DOCTYPE html>
<html lang="en">
<head>
<meta charset="utf-8">
<title>Lodgewell Business Card</title>
<link href="https://fonts.googleapis.com/css2?family=Arimo:wght@400;700&display=swap" rel="stylesheet">
<style>
  :root {
    --brand-orange: #e8923c;
    --ink: #231f20;
    --paper: #ffffff;
    --card-edge: #6d6e71;
    --rule: #808285;
  }
  html, body {
    margin: 0;
    padding: 0;
    width: 1200px;
    height: 1200px;
    overflow: hidden;
    background: var(--paper);
    font-family: "Arimo", Arial, sans-serif;
  }
  .canvas {
    position: relative;
    width: 1200px;
    height: 1200px;
  }
  .card {
    position: absolute;
    left: 180px;
    width: 838px;
    height: 478px;
    border-radius: 40px;
    box-sizing: border-box;
  }
  .card--front {
    top: 100px;
    background: var(--brand-orange);
    color: var(--paper);
  }
  .card--back {
    top: 619px;
    background: var(--paper);
    border: 1px solid var(--card-edge);
  }
  .wordmark {
    position: absolute;
    font-weight: 700;
    letter-spacing: -0.05em;
    line-height: 1;
    white-space: nowrap;
  }
  .wordmark .tm {
    font-size: 0.09em;
    letter-spacing: 0;
    vertical-align: top;
    position: relative;
    top: 0.3em;
    margin-left: 0.3em;
  }
  .card--front .wordmark {
    left: 0;
    right: 0;
    top: 172px;
    text-align: center;
    font-size: 132px;
  }
  .tagline {
    position: absolute;
    left: 0;
    right: 0;
    top: 374px;
    margin: 0;
    text-align: center;
    font-size: 25px;
    font-weight: 700;
    letter-spacing: 0.04em;
  }
  .card--back .wordmark {
    left: 106px;
    top: 64px;
    font-size: 104px;
    color: var(--brand-orange);
  }
  .contact-block {
    position: absolute;
    left: 296px;
    top: 235px;
    height: 198px;
    padding-left: 33px;
    border-left: 2px solid var(--rule);
    color: var(--ink);
  }
  .contact-names {
    margin: 4px 0 0;
    font-size: 32px;
    font-weight: 700;
  }
  .contact-role {
    margin: 6px 0 18px;
    font-size: 22px;
  }
  .contact-list {
    list-style: none;
    margin: 0;
    padding: 0;
  }
  .contact-list li {
    display: flex;
    align-items: center;
    height: 36px;
    font-size: 26px;
  }
  .contact-list svg {
    width: 26px;
    height: 26px;
    margin-right: 10px;
    flex: none;
  }
</style>
</head>
<body>
<div class="canvas">
  <section class="card card--front">
    <div class="wordmark">Lodgewell<span class="tm">TM</span></div>
    <p class="tagline">Holiday Let Management &amp; Consulting Specialists</p>
  </section>

  <section class="card card--back">
    <div class="wordmark">Lodgewell<span class="tm">TM</span></div>
    <div class="contact-block">
      <p class="contact-names">Marta Van Kerr Owen Brisk</p>
      <p class="contact-role">Principal Director</p>
      <ul class="contact-list">
        <li>
          <svg viewBox="0 0 26 26" aria-hidden="true">
            <rect x="7" y="2" width="12" height="21" rx="2.5" fill="none" stroke="var(--brand-orange)" stroke-width="2.5"/>
            <circle cx="13" cy="19" r="1.5" fill="var(--brand-orange)"/>
          </svg>
          0492637058 0487350216
        </li>
        <li>
          <svg viewBox="0 0 26 26" aria-hidden="true">
            <rect x="1" y="6" width="24" height="14" fill="var(--brand-orange)"/>
            <path d="M1 6 L13 14 L25 6 M1 20 L10 12 M25 20 L16 12" fill="none" stroke="var(--paper)" stroke-width="1.5"/>
          </svg>
          enquiries@lodgewell.com.au
        </li>
        <li>
          <svg viewBox="0 0 26 26" aria-hidden="true">
            <g fill="none" stroke="var(--brand-orange)" stroke-width="2">
              <circle cx="13" cy="13" r="10.5"/>
              <ellipse cx="13" cy="13" rx="4.5" ry="10.5"/>
              <path d="M2.5 13 H23.5 M4.5 7.5 H21.5 M4.5 18.5 H21.5"/>
            </g>
          </svg>
          www.lodgewell.com.au
        </li>
      </ul>
    </div>
  </section>
</div>
</body>
</html>
```